Allied Health business card / Logo update.

Update/revitalise our logo and business cards. The logo needs to be suitable not only for business cards but stationary, website and clothing as well.

We have had the same hand logo for 16 years and have a strong brand name with this. One idea, however, was to base the idea around the similarities between the spine and bamboo. I will attach some images.

We are uncertain with colour. Initially, we thought earthy greens and greys/charcoal. However, we would also consider blue/charcoal combination.

I have attached our existing logo and this is our website. http://www.ridgewaybackclinic.com.au

Target Market(s)

General public
This is the only card

Industry/Entity Type

Health Care

Contact Information for Business Card

Ridgeway Backcare Centre
27 Hillview Road (Cnr Belford St and Hillview Rd) Port Ardmore
5/18 Tindall St Kelbrook
phone: 02 6471 2856
email: info@ridgewaybackclinic.com.au
web: ridgewaybackclinic.com.au

Martin K. Lowe
Cert. Rehab Therapist
Chiropractor
BSc(Hon)., MChirop(Adv)., MClinRehabNeuro(Res)
MRBP, MTSKE, OLUX

Font styles to use
Serif
Sans Serif

Colors
acd037
85acd3
5c5c5c

Requirements
Must have
• Company name, Professional name with qualifications
• Contact details.

```html
<!DOCTYPE html>
<html lang="en">
<head>
<meta charset="utf-8">
<title>Ridgeway Backcare Centre – Business Card</title>
<link rel="stylesheet" href="https://fonts.googleapis.com/css2?family=Montserrat:wght@600;700&family=Open+Sans:wght@400;600&display=swap">
<style>
  :root {
    --green: #acd037;
    --green-pale: #e6f0c4;
    --charcoal: #5c5c5c;
    --charcoal-dark: #4a4a4a;
    --paper: #ffffff;
    --backdrop: #ecebe6;
    --band-text: #ffffff;
  }
  * { box-sizing: border-box; margin: 0; padding: 0; }
  html, body {
    width: 1200px; height: 1023px; overflow: hidden;
    background: var(--backdrop);
  }
  .card {
    position: absolute; left: 150px; top: 241px;
    width: 900px; height: 540px;
    background: var(--paper);
    border-radius: 34px;
    overflow: hidden;
    box-shadow: 0 10px 30px rgba(0,0,0,0.12);
  }
  .card__decoration {
    position: absolute; right: 0; top: 0;
    width: 430px; height: 340px;
    background: radial-gradient(ellipse at 60% 45%, var(--green-pale) 0%, rgba(230,240,196,0.45) 45%, rgba(255,255,255,0) 75%);
  }
  .brand-mark {
    position: absolute; left: 44px; top: 110px;
    width: 180px; height: 180px; border-radius: 50%;
    background: var(--charcoal);
    border: 5px solid var(--green);
  }
  .identity {
    position: absolute; left: 256px; top: 50px;
  }
  .company-name {
    font-family: 'Montserrat', sans-serif; font-weight: 700;
    line-height: 1.02; text-transform: uppercase;
  }
  .company-name span { display: block; }
  .company-name .line-sm { font-size: 30px; color: var(--charcoal); }
  .company-name .line-lg { font-size: 58px; letter-spacing: 0.5px; color: var(--green); }
  .practitioner {
    margin-top: 16px;
    font-family: 'Montserrat', sans-serif; font-weight: 700;
    font-size: 32px; color: var(--green); text-transform: uppercase;
  }
  .credentials {
    margin-top: 6px;
    font-family: 'Open Sans', sans-serif; font-size: 18px;
    line-height: 1.35; color: var(--charcoal);
  }
  .divider {
    position: absolute; left: 0; right: 0; top: 360px; height: 14px;
    background: var(--charcoal-dark);
  }
  .contact-band {
    position: absolute; left: 0; right: 0; top: 374px; bottom: 0;
    background: var(--green);
    display: grid;
    grid-template-columns: 1fr 28px 1fr;
    column-gap: 14px; row-gap: 10px;
    align-content: center;
    padding: 0 40px;
    font-family: 'Open Sans', sans-serif; font-size: 19px;
    color: var(--band-text);
  }
  .contact-band .left { text-align: right; }
  .contact-band .icon { width: 26px; height: 26px; align-self: center; }
</style>
</head>
<body>
  <section class="card">
    <div class="card__decoration" role="img" aria-label="Faint pale green bamboo leaves and spine pattern"></div>

    <div class="brand-mark" aria-hidden="true"></div>

    <div class="identity">
      <h1 class="company-name">
        <span class="line-sm">Ridgeway</span>
        <span class="line-lg">Backcare</span>
        <span class="line-sm">Centre</span>
      </h1>
      <p class="practitioner">Martin K. Lowe</p>
      <p class="credentials">
        Cert. Rehab Therapist<br>
        Chiropractor<br>
        BSc(Hon)., MChirop(Adv)., MClinRehabNeuro(Res)<br>
        MRBP, MTSKE, OLUX
      </p>
    </div>

    <div class="divider"></div>

    <div class="contact-band">
      <span class="left">02 6471 2856</span>
      <svg class="icon" viewBox="0 0 26 26" aria-hidden="true">
        <circle cx="13" cy="13" r="12" fill="#fff"/>
        <path d="M8.5 7.5c1-.8 1.8-.6 2.3.3l.9 1.7c.3.6.1 1.1-.4 1.5l-.7.5c.6 1.5 1.8 2.8 3.4 3.5l.5-.7c.4-.5 1-.7 1.5-.4l1.7.9c.9.5 1.1 1.3.3 2.3-1.2 1.4-3 1.3-5.3-.2-2.2-1.5-3.8-3.5-4.6-5.7-.5-1.6-.4-2.9.4-3.7z" fill="#acd037"/>
      </svg>
      <span>27 Hillview Road</span>

      <span class="left">info@ridgewaybackclinic.com.au</span>
      <svg class="icon" viewBox="0 0 26 26" aria-hidden="true">
        <circle cx="13" cy="13" r="12" fill="#fff"/>
        <rect x="7" y="8.5" width="12" height="9" rx="1" fill="#acd037"/>
        <path d="M7.5 9.2 13 13.5l5.5-4.3" stroke="#fff" stroke-width="1.3" fill="none"/>
      </svg>
      <span>(Cnr Belford St and Hillview Rd)</span>

      <span class="left">ridgewaybackclinic.com.au</span>
      <svg class="icon" viewBox="0 0 26 26" aria-hidden="true">
        <circle cx="13" cy="13" r="12" fill="#fff"/>
        <circle cx="13" cy="13" r="6.5" fill="none" stroke="#acd037" stroke-width="1.5"/>
        <ellipse cx="13" cy="13" rx="2.8" ry="6.5" fill="none" stroke="#acd037" stroke-width="1.3"/>
        <path d="M6.5 13h13" stroke="#acd037" stroke-width="1.3"/>
      </svg>
      <span>Port Ardmore 5/18 Tindall St Kelbrook</span>
    </div>
  </section>
</body>
</html>
```